Modern home page design for a Dental Surgery

- This design will have a 5 day deadline only.

- The design must be based around the attached HPID (home page information design) called LUMA HPID. I've attached Word and PDF versions - these are the same. The table boxes are just for approximate placement of information – you DON'T have to make it look exactly like this. All fonts used in the HPID are only examples - you can use any Google font you wish.

- Information only is in orange text. Copy to go on the design in black text. Some instructions are in the HPID. Please be creative!

- The design needs to be modern. Colours are to be black and white with grey and blue like the logo colours. Background white please.

- I've provided the images for the galleries - they are labelled and will match the name in the HPID.

- I've provided icons for the items below the gallery - the name of the image will match the subheading for each section. You can use other icons if you want to.

- This is a website that is an example of what we like. Please DON'T copy this exactly though!
http://brightmolarclinic.example.co.nz/

Width of content will be 1100 pixels when implemented as a web page. Header height (without nav bar) 150-160 pixels.

If your design is chosen the winning PSD file will have to be provided as follows…
1. Canvas size of 2000px x 2000px - 72ppi in Adobe Photoshop (CS5 compatible)
2. Width of content section is 1100px wide - centered in the canvas
3. Any button rollovers/hovers in the PSD as hidden layers.
4. All fonts used must be Google fonts (except for the fonts in the header at the top of the page).
5. You will need to supply the chosen home page plus one example page (example page as a style guide for how all other pages will look). Example page is only the header and navigational bar at the top, an empty sector in the middle with a column (180 px wide) which can be left or right aligned which means the main sector is 920 pixels wide, and then the footer at the bottom of the page
Updates

Hi Designers, The 1st posted deadline for this project was incorrect; please note new deadline for November 22.

Target Market(s)

all ages that need dental care

Industry/Entity Type

Dental

Number of Pages Required

1 page

Font styles to use
Sans Serif

Requirements
Must have
• modern clean design - as per the Project Description
Should not have
• should not be cluttered. Just because I use tables to show information placement on the HPID - you do NOT have to use boxes around information in the design.

```html
<!DOCTYPE html>
<html lang="en">
<head>
<meta charset="utf-8">
<title>Northridge Family Dentistry</title>
<link rel="stylesheet" href="https://fonts.googleapis.com/css2?family=Montserrat:wght@400;500;600;700&family=Roboto:wght@300;400;500&display=swap">
<style>
:root{
  --blue:#14518f;
  --blue-accent:#2f8fd6;
  --ink:#1b1b1b;
  --text:#333;
  --grey-band:#e4e4e4;
  --grey-bar:#b9b9b9;
  --white:#fff;
}
*{margin:0;padding:0;box-sizing:border-box}
html,body{width:1200px;height:2203px;overflow:hidden;background:var(--white)}
body{font-family:"Roboto",Arial,sans-serif;color:var(--text);position:relative}
.abs{position:absolute}

/* header */
.site-header{position:absolute;left:0;top:0;width:1200px;height:140px}
.brand{left:96px;top:20px;width:176px;height:100px;display:flex;align-items:center;gap:10px}
.brand-dot{width:14px;height:14px;border-radius:50%;background:var(--blue)}
.brand-name{font-family:"Montserrat",sans-serif;font-weight:600;font-size:22px;color:var(--blue)}
.practice{left:292px;top:28px;font-family:"Montserrat",sans-serif;font-weight:400;font-size:21px;line-height:28px;color:#6b6b6b}
.header-phone{right:80px;top:52px;display:flex;align-items:center;gap:8px;font-family:"Montserrat",sans-serif;font-weight:500;font-size:26px;color:var(--blue)}

/* nav */
.main-nav{position:absolute;left:0;top:141px;width:1200px;height:47px;background:linear-gradient(#2a74bf,#125096);display:flex;padding-left:50px}
.main-nav a{display:flex;align-items:center;justify-content:center;height:47px;color:var(--white);font-size:15px;text-decoration:none;border-right:1px solid rgba(0,0,0,.25)}
.main-nav a:first-child,.main-nav a:last-child{border-right:none}

/* hero */
.hero{position:absolute;left:0;top:188px;width:1200px;height:437px;background:linear-gradient(90deg,#f3f3f3 0%,#ebeeef 45%,#dfe6e8 70%,#eef0f1 100%)}
.hero-title{left:85px;top:188px;font-family:"Montserrat",sans-serif;font-weight:700;font-size:27px;color:var(--blue);letter-spacing:.3px}
.hero-sub{left:85px;top:224px;font-family:"Montserrat",sans-serif;font-size:23px;color:#222}

/* intro */
.intro{position:absolute;top:674px;width:480px;text-align:center}
.intro-icon{display:block;width:100px;height:100px;margin:0 auto}
.intro h2{margin-top:16px;font-family:"Roboto",sans-serif;font-weight:400;font-size:18px;line-height:22px;color:var(--ink)}
.intro p{margin-top:10px;font-size:13px;line-height:19px;color:#222}
.btn-solid{display:inline-block;margin-top:18px;background:var(--blue);color:var(--white);font-size:15px;font-weight:500;padding:0 18px;height:37px;line-height:37px;border-radius:2px;text-decoration:none}

/* feature cards */
.card{position:absolute;top:990px;width:344px;height:263px;text-align:center;padding-top:20px}
.card.solid{background:var(--blue);color:var(--white)}
.card.plain{color:var(--blue)}
.card h3{margin-top:10px;font-family:"Roboto",sans-serif;font-weight:500;font-size:21px}
.card p{margin:16px auto 0;width:310px;font-size:13px;line-height:19px}
.card.plain p{color:#444}
.btn-outline{display:inline-block;margin-top:14px;height:36px;line-height:32px;padding:0 16px;border:2px solid currentColor;border-radius:3px;font-size:14px;font-weight:500;text-decoration:none;color:inherit;background:transparent}
.card.solid .btn-outline{color:var(--white)}
.card.plain .btn-outline{color:var(--blue);border-width:1.5px}

/* emergency */
.emergency{position:absolute;left:0;top:1300px;width:1200px;height:273px;background:linear-gradient(180deg,#e8eaeb,#f1f2f3 50%,#e6e8e9);text-align:center}
.emergency h2{margin-top:90px;font-family:"Montserrat",sans-serif;font-weight:600;font-size:26px;letter-spacing:2px;color:var(--ink)}
.emergency p{margin:18px auto 0;width:990px;font-size:12.5px;line-height:19px;color:#222}
.emergency .phone{margin-top:16px;display:inline-flex;align-items:center;gap:10px;font-family:"Montserrat",sans-serif;font-weight:600;font-size:29px;color:var(--blue-accent)}

/* associations */
.assoc-title{position:absolute;left:84px;top:1618px;width:1032px;height:30px;display:flex;align-items:center;gap:18px}
.assoc-title::before,.assoc-title::after{content:"";flex:1;height:1px;background:#dcdcdc}
.assoc-title span{font-family:"Roboto",sans-serif;font-size:26px;color:var(--ink)}
.badge{position:absolute;top:1689px}
.badge.oval{width:104px;height:68px;border-radius:50%;background:radial-gradient(#1f8f8a,#0e4f57)}
.badge.rect{width:90px;height:50px;top:1698px;border:2px solid #d55;border-radius:3px}

/* footer */
.site-footer{position:absolute;left:0;top:1804px;width:1200px;height:361px;background:var(--grey-band)}
.fcol{position:absolute;top:36px;font-size:12.5px;line-height:24.4px;color:#333}
.fcol.cont{top:66px}
.fcol h4{font-family:"Roboto",sans-serif;font-weight:500;font-size:15.5px;color:var(--blue-accent);display:inline-block;border-bottom:1px solid var(--blue-accent);line-height:22px;margin-bottom:8px}
.fcol ul{list-style:none}
.fcol .l2{padding-left:10px;color:#555;font-size:12px}
.fcol .l3{padding-left:22px;color:#999;font-size:11.5px}
.copyright{position:absolute;left:0;top:2165px;width:1200px;height:38px;background:var(--grey-bar);text-align:center;line-height:38px;font-size:12px;color:#222}
</style>
</head>
<body>

<header class="site-header">
  <div class="abs brand"><span class="brand-dot"></span><span class="brand-name">Luma Group</span></div>
  <div class="abs practice">Northridge<br>Family Dentistry<br>NORTHRIDGE</div>
  <div class="abs header-phone">
    <svg width="14" height="26" viewBox="0 0 14 26"><path d="M11 2 C4 3 2 8 2 13 C2 18 4 23 11 24" fill="none" stroke="currentColor" stroke-width="4" stroke-linecap="round"/></svg>
    04 555 0182
  </div>
</header>

<nav class="main-nav">
  <a href="#" style="width:118px">Home</a>
  <a href="#" style="width:105px">About</a>
  <a href="#" style="width:157px">What We Do</a>
  <a href="#" style="width:177px">Why Chose Us</a>
  <a href="#" style="width:133px">Services</a>
  <a href="#" style="width:94px">Cost</a>
  <a href="#" style="width:169px">Appointment</a>
  <a href="#" style="width:117px">Contact</a>
</nav>

<section class="hero" role="img" aria-label="Bright dental surgery room with a teal patient chair and equipment">
  <div class="abs hero-title">YOUR LOCAL DENTAL SURGERY</div>
  <div class="abs hero-sub">Halden &amp; Northridge</div>
</section>

<section class="intro" style="left:102px">
  <svg class="intro-icon" viewBox="0 0 100 100"><circle cx="50" cy="50" r="46" fill="#fff" stroke="#14518f" stroke-width="7"/><path d="M38 30 C42 26 46 30 50 30 C54 30 58 26 62 30 C66 36 62 44 60 52 C58 60 56 66 54 66 C52 66 52 56 50 56 C48 56 48 66 46 66 C44 66 42 60 40 52 C38 44 34 36 38 30Z" fill="#2f8fd6"/><path d="M30 40 C30 62 44 72 54 74 C64 76 70 70 70 64" fill="none" stroke="#14518f" stroke-width="3"/><circle cx="70" cy="62" r="4" fill="#14518f"/></svg>
  <h2>What We Do</h2>
  <p>The Luma Dental Centre offer a wide range of dental services including diagnostics, orthodontics, dentures, oral surgery, and periodontal, root canal and cosmetic dentistry.</p>
  <a class="btn-solid" href="#">READ MORE &gt;&gt;</a>
</section>

<section class="intro" style="left:618px">
  <svg class="intro-icon" viewBox="0 0 100 100"><circle cx="50" cy="50" r="46" fill="#fff" stroke="#14518f" stroke-width="7"/><path d="M36 28 C41 24 46 29 50 29 C54 29 59 24 64 28 C70 34 66 46 63 56 C61 64 59 72 56 72 C53 72 53 60 50 60 C47 60 47 72 44 72 C41 72 39 64 37 56 C34 46 30 34 36 28Z" fill="none" stroke="#14518f" stroke-width="3"/><path d="M42 46 L49 53 L62 38" fill="none" stroke="#2f8fd6" stroke-width="4" stroke-linecap="round"/></svg>
  <h2>How Much Does It Cost ?</h2>
  <p>Find out estimates of how much each dental procedure costs. (Exact prices will be discussed with you after consultation depending on your specific dental requirements.)</p>
  <a class="btn-solid" href="#">VIEW COST &gt;&gt;</a>
</section>

<article class="card solid" style="left:84px">
  <svg width="60" height="62" viewBox="0 0 60 62"><rect x="10" y="4" width="14" height="20" rx="2" fill="#fff"/><path d="M8 40 L30 40 L48 20 L52 24 L34 46 L8 46Z" fill="#fff"/><rect x="14" y="48" width="6" height="12" fill="#fff"/><rect x="6" y="56" width="24" height="4" fill="#fff"/></svg>
  <h3>Make An Appoitment</h3>
  <p>Two convenient locations in Halden and Northridge offer dental services for all ages. Take a moment to book your appointment</p>
  <a class="btn-outline" href="#">MAKE APPOINTMENT</a>
</article>

<article class="card plain" style="left:428px">
  <svg width="60" height="62" viewBox="0 0 60 62"><path d="M16 10 C22 4 28 10 32 10 C36 10 42 4 48 10 C54 18 48 30 46 40 C44 50 42 58 39 58 C36 58 36 46 32 46 C28 46 28 58 25 58 C22 58 20 50 18 40 C16 30 10 18 16 10Z" fill="none" stroke="#14518f" stroke-width="3"/><circle cx="16" cy="18" r="10" fill="#fff" stroke="#14518f" stroke-width="4"/><line x1="10" y1="26" x2="2" y2="38" stroke="#14518f" stroke-width="4" stroke-linecap="round"/></svg>
  <h3>Your First Consultaion</h3>
  <p>Want to know what will happen in your first consultation? Check out our first dental consultation process.</p>
  <a class="btn-outline" href="#">FIRST CONSULTATION</a>
</article>

<article class="card solid" style="left:773px">
  <svg width="60" height="62" viewBox="0 0 60 62"><rect x="8" y="8" width="44" height="52" rx="3" fill="none" stroke="#fff" stroke-width="4"/><rect x="20" y="3" width="20" height="10" rx="2" fill="#fff"/><g fill="#fff"><rect x="16" y="22" width="4" height="4"/><rect x="24" y="22" width="20" height="4"/><rect x="16" y="32" width="4" height="4"/><rect x="24" y="32" width="20" height="4"/><rect x="16" y="42" width="4" height="4"/><rect x="24" y="42" width="20" height="4"/></g></svg>
  <h3>Application Form</h3>
  <p>Save time and fill in an online application form (or download, print out and complete) before your first visit.</p>
  <a class="btn-outline" href="#">APPLICATION FORM</a>
</article>

<section class="emergency" role="region" aria-label="Emergency">
  <svg class="abs" style="left:570px;top:19px" width="60" height="60" viewBox="0 0 60 60"><path d="M16 8 C22 2 28 8 32 8 C36 8 42 2 48 8 C54 16 48 28 46 38 C44 48 42 56 39 56 C36 56 36 44 32 44 C28 44 28 56 25 56 C22 56 20 48 18 38 C16 28 10 16 16 8Z" fill="none" stroke="#14518f" stroke-width="3"/><path d="M2 20 L20 20 L24 30 L14 34 Z" fill="#14518f"/></svg>
  <h2>IS THIS AN EMERGENCY ?</h2>
  <p>Lorem Ipsum is simply dummy text of the printing and typesetting industry. Lorem Ipsum has been the industry's standard dummy text. Lorem Ipsum is simply dummy text of the printing and typesetting industry. Lorem Ipsum has been the industry's standard dummy text. Lorem Ipsum is simply dummy text of the printing and industry. Lorem Ipsum has been the industry's standard dummy text.</p>
  <div class="phone">
    <svg width="14" height="28" viewBox="0 0 14 28"><path d="M11 2 C4 3 2 9 2 14 C2 19 4 25 11 26" fill="none" stroke="currentColor" stroke-width="4" stroke-linecap="round"/></svg>
    04 555 0182
  </div>
</section>

<div class="assoc-title"><span>Associations</span></div>
<div class="badge oval" style="left:84px"></div>
<div class="badge rect" style="left:272px"></div>
<div class="badge oval" style="left:458px"></div>
<div class="badge rect" style="left:665px"></div>
<div class="badge oval" style="left:850px"></div>
<div class="badge rect" style="left:1028px"></div>

<footer class="site-footer">
  <div class="fcol" style="left:85px">
    <h4>SITE LINKS</h4>
    <ul>
      <li>Home</li><li>About</li>
      <li class="l2">Team</li><li class="l2">Registration</li>
      <li>What We Do</li><li>Why Chose Us</li>
      <li class="l2">Testimonials</li>
      <li>Cost</li><li>Appointment</li><li>Contact / Map</li>
    </ul>
  </div>
  <div class="fcol" style="left:275px">
    <h4>SERVICES</h4>
    <ul>
      <li>Restorative Dentistry</li>
      <li class="l2">Preventative</li>
      <li class="l3">Fissure Sealants</li><li class="l3">Mouthguards</li><li class="l3">Bite Splints</li>
      <li class="l2">Fillings</li>
      <li class="l3">Amalgams, Composites (white fillings)</li><li class="l3">Porcelain &amp; Gold</li>
      <li class="l2">Crown &amp; Bridge Treatment</li>
      <li class="l2">Implants</li>
    </ul>
  </div>
  <div class="fcol cont" style="left:598px">
    <ul>
      <li>Oral Surgery</li>
      <li class="l2">Extractions</li><li class="l2">Minor Impacted Wisdom Teeth</li>
      <li>Periodontal (gum) Care</li>
      <li class="l2">Hygiene Service</li><li class="l2">Minor Periodonatal Surgery</li><li class="l2">Preventive Services</li>
      <li>Root Canal Therapy</li>
      <li>Cosmetic</li>
      <li class="l2">Porcelain Veneers</li><li class="l2">Brightline Bleaching</li>
    </ul>
  </div>
  <div class="fcol cont" style="left:899px">
    <ul>
      <li>Orthodontics</li>
      <li>Children &amp; pre-schoolers</li>
      <li class="l2">Free Secondary School Dentistry</li>
      <li class="l3">Free Dental Care Under 18</li>
      <li class="l2">Pre-school Dentistry</li>
      <li>Oral Care Products</li>
      <li>Diagnostic Dentistry</li>
      <li class="l2">Digital X-rays</li><li class="l2">Panoramic X-rays</li><li class="l2">Intra-oral photography &amp; Camera</li><li class="l2">Laser Cavity Detection</li>
    </ul>
  </div>
</footer>
<div class="copyright">Copyright © 2014- Luma Group</div>

</body>
</html>
```